Need Business cards

Im a new realtor and already have a logo. I would like to purchase a Business card design that catches customer's attention, its creative, and modern.

Marisol Quintero
Realtor ®
(555) 318 4027
marisolqtrhomes@brindlemail.com

Target Market(s)

investors, buyers and seller, property management

Industry/Entity Type

real estate,

Contact Information for Business Card

Marisol Quintero

Requirements
Must have
• BOTH LOGOS, WOULD LIKE TO SEE WITH DIFFERENT OPTIONS WITH EITHER PICTURE

```html
<!DOCTYPE html>
<html lang="en">
<head>
<meta charset="utf-8">
<title>Marisol Quintero – Business Cards</title>
<link href="https://fonts.googleapis.com/css2?family=Poppins:wght@400;500;600;700&display=swap" rel="stylesheet">
<style>
  :root {
    --navy: #0c2d52;
    --navy-soft: #1a3e68;
    --white: #ffffff;
    --gold: #c39a35;
    --ink: #1c2430;
    --stage: #eceef1;
    --brand-blue: #2f6fb3;
  }
  * { margin: 0; padding: 0; box-sizing: border-box; }
  html, body { width: 1200px; height: 800px; overflow: hidden; }
  body {
    background: var(--stage);
    font-family: "Poppins", sans-serif;
    position: relative;
  }
  .card {
    position: absolute;
    top: 240px;
    width: 560px;
    height: 320px;
    border-radius: 4px;
    overflow: hidden;
    box-shadow: 0 6px 18px rgba(12, 45, 82, 0.18);
  }
  .card svg.card-art { position: absolute; inset: 0; }
  .card-front { left: 25px; background: var(--navy); }
  .card-back { left: 615px; background: var(--white); }

  .portrait {
    position: absolute;
    left: 270px; top: 25px;
    width: 160px; height: 160px;
    border-radius: 50%;
    background: radial-gradient(circle at 50% 45%, #e6cfa8 0%, #c9a874 35%, var(--navy-soft) 72%, var(--navy) 100%);
  }
  .nameplate {
    position: absolute;
    left: 90px; top: 202px;
    text-align: left;
  }
  .nameplate-name {
    color: var(--gold);
    font-weight: 600;
    font-size: 17px;
    letter-spacing: 0.3px;
    text-transform: uppercase;
  }
  .nameplate-title {
    color: var(--ink);
    font-size: 10px;
    font-weight: 500;
    margin-left: 50px;
    margin-top: -3px;
  }

  .brokerage {
    position: absolute;
    left: 38px; top: 58px;
    color: var(--brand-blue);
    font-weight: 700;
    font-size: 22px;
    letter-spacing: 0.5px;
    text-transform: uppercase;
  }
  .contact {
    position: absolute;
    left: 36px; top: 198px;
    list-style: none;
    color: var(--navy);
    font-size: 15px;
    font-weight: 500;
  }
  .contact li { display: flex; align-items: center; gap: 9px; height: 30px; }
  .contact svg { width: 14px; height: 14px; fill: var(--gold); flex: none; }
  .emblem {
    position: absolute;
    left: 348px; top: 78px;
    width: 184px; height: 184px;
    display: flex; flex-direction: column;
    align-items: center; justify-content: center;
    text-align: center;
  }
  .emblem-name {
    color: var(--gold);
    font-weight: 600;
    font-size: 19px;
    line-height: 1.25;
    text-transform: uppercase;
  }
</style>
</head>
<body>

  <section class="card card-front" aria-label="Card front">
    <svg class="card-art" width="560" height="320" viewBox="0 0 560 320">
      <path d="M430 40 L470 0 L515 0 L440 75 Z" fill="#ffffff"/>
      <path d="M0 198 L250 170 Q275 165 285 185 L290 195 L292 232 L0 262 Z" fill="#ffffff"/>
      <circle cx="350" cy="105" r="96" fill="#ffffff"/>
    </svg>
    <div class="portrait" role="img" aria-label="Portrait photo of the realtor in a light blazer"></div>
    <div class="nameplate">
      <p class="nameplate-name">Marisol Quintero</p>
      <p class="nameplate-title">Realtor ®</p>
    </div>
  </section>

  <section class="card card-back" aria-label="Card back">
    <svg class="card-art" width="560" height="320" viewBox="0 0 560 320">
      <path d="M0 262 L300 262 Q340 262 345 240 L360 190 L560 190 L560 320 L0 320 Z" fill="var(--navy)"/>
      <path d="M520 240 L560 270 L560 320 L500 320 Z" fill="var(--navy)"/>
      <circle cx="440" cy="170" r="108" fill="var(--navy)"/>
      <circle cx="440" cy="170" r="94" fill="#ffffff"/>
    </svg>
    <p class="brokerage">Northvale Realty</p>
    <ul class="contact">
      <li>
        <svg viewBox="0 0 24 24" aria-hidden="true"><path d="M6.6 10.8a15.1 15.1 0 0 0 6.6 6.6l2.2-2.2a1 1 0 0 1 1-.25 11.4 11.4 0 0 0 3.6.57 1 1 0 0 1 1 1V20a1 1 0 0 1-1 1A17 17 0 0 1 3 4a1 1 0 0 1 1-1h3.5a1 1 0 0 1 1 1c0 1.25.2 2.45.57 3.6a1 1 0 0 1-.25 1z"/></svg>
        (555) 318 4027
      </li>
      <li>
        <svg viewBox="0 0 24 24" aria-hidden="true"><path d="M2 5h20v14H2z M3.5 6.5 12 13l8.5-6.5" fill="var(--gold)" stroke="#ffffff" stroke-width="1.4"/></svg>
        marisolqtrhomes@brindlemail.com
      </li>
    </ul>
    <div class="emblem">
      <p class="emblem-name">Marisol<br>Quintero</p>
    </div>
  </section>

</body>
</html>
```